Environmentally conscious Waste Management Company requires business card

We Require a Business card for our environmentally conscious waste management company . The business card should have a very clean design. be double sided and incorporate our logo..
The card will need o have 9 lines for the contact details - that are
Name
Title
Business
Address Line 1
Address Line 2
Address Line 3
Phone
Mobile
Email

Industry/Entity Type

Waste Management

Font styles to use
Other font styles liked:
• Helvetica or similar

```html
<!DOCTYPE html>
<html lang="en">
<head>
<meta charset="utf-8">
<title>Terrawise business card</title>
<link href="https://fonts.googleapis.com/css2?family=Roboto:wght@400;500&family=Oswald:wght@600&display=swap" rel="stylesheet">
<style>
  :root{
    --green:#14c22c;
    --green-light:#5fdc6f;
    --white:#ffffff;
    --ink:#2b2b2b;
    --backdrop:#3a3a3a;
  }
  *{margin:0;padding:0;box-sizing:border-box;}
  html,body{width:1200px;height:903px;overflow:hidden;background:var(--backdrop);}
  body{position:relative;font-family:"Roboto",Helvetica,Arial,sans-serif;}

  .card{position:absolute;left:250px;width:700px;height:400px;background:var(--white);overflow:hidden;box-shadow:0 10px 30px rgba(0,0,0,.45);}
  .card--front{top:40px;}
  .card--back{top:463px;}

  .band{position:absolute;left:0;width:100%;}

  /* front */
  .front__top{top:0;height:78px;background:var(--green);}
  .front__top-stripe{top:78px;height:18px;background:var(--green-light);}
  .front__bottom-stripe{bottom:78px;height:18px;background:var(--green-light);}
  .front__bottom{bottom:0;height:78px;background:var(--green);}

  .brand-name{position:absolute;color:var(--green);font-family:"Roboto",Helvetica,Arial,sans-serif;font-weight:400;line-height:1;white-space:nowrap;}
  .card--front .brand-name{left:50%;top:50%;transform:translate(-50%,-50%);font-size:54px;}

  /* back */
  .back__top{top:0;height:22px;background:var(--green);}
  .back__top-stripe{top:22px;height:8px;background:var(--green-light);}
  .address{position:absolute;right:30px;top:52px;text-align:right;color:var(--ink);font-size:19px;line-height:1.35;letter-spacing:.5px;}
  .card--back .brand-name{left:36px;top:150px;font-size:56px;}
  .back__rule{top:232px;height:6px;background:var(--green);}

  .person{position:absolute;left:0;top:250px;width:430px;height:120px;background:var(--green);padding:28px 0 0 40px;color:var(--white);}
  .person__name{font-family:"Oswald",Impact,sans-serif;font-weight:600;font-size:36px;letter-spacing:1px;line-height:1;}
  .person__title{font-size:14px;letter-spacing:2px;margin-top:6px;}

  .contact-panel{position:absolute;left:430px;top:150px;width:270px;height:220px;background:var(--green-light);}
  .contact-box{position:absolute;left:26px;top:24px;width:222px;height:156px;background:var(--green);padding:18px 16px;}
  .contact-list{list-style:none;display:flex;flex-direction:column;gap:14px;}
  .contact-list li{display:flex;justify-content:flex-end;align-items:center;gap:8px;color:var(--white);font-size:12px;letter-spacing:.4px;white-space:nowrap;}
  .contact-list svg{width:18px;height:18px;flex:none;}

  .back__bottom{bottom:0;height:14px;background:var(--green);}
</style>
</head>
<body>

<section class="card card--front" aria-label="Card front">
  <div class="band front__top"></div>
  <div class="band front__top-stripe"></div>
  <p class="brand-name">Terrawise</p>
  <div class="band front__bottom-stripe"></div>
  <div class="band front__bottom"></div>
</section>

<section class="card card--back" aria-label="Card back">
  <div class="band back__top"></div>
  <div class="band back__top-stripe"></div>

  <p class="address">42 Fernleaf Road,<br>5th Block Lane E.</p>

  <p class="brand-name">Terrawise</p>

  <div class="band back__rule"></div>

  <div class="person">
    <p class="person__name">MARA QUILL</p>
    <p class="person__title">GENERAL MANAGER</p>
  </div>

  <div class="contact-panel">
    <div class="contact-box">
      <ul class="contact-list">
        <li>014 552 3870
          <svg viewBox="0 0 18 18" aria-hidden="true"><rect width="18" height="18" rx="3" fill="#fff"/><path d="M5 4.5l2 0 1 2.5-1.3 1a6 6 0 0 0 3.3 3.3l1-1.3 2.5 1v2c0 .5-.5 1-1 1A9 9 0 0 1 4 5.5c0-.5.5-1 1-1z" fill="#14c22c"/></svg>
        </li>
        <li>014 552 3871
          <svg viewBox="0 0 18 18" aria-hidden="true"><rect width="18" height="18" rx="3" fill="#fff"/><rect x="6" y="3.5" width="6" height="11" rx="1" fill="#14c22c"/><rect x="7" y="5" width="4" height="7" fill="#fff"/></svg>
        </li>
        <li>hello@terrawise.co
          <svg viewBox="0 0 18 18" aria-hidden="true"><rect width="18" height="18" rx="3" fill="#fff"/><rect x="3.5" y="5.5" width="11" height="7.5" fill="#14c22c"/><path d="M3.5 5.5l5.5 4.5 5.5-4.5" fill="none" stroke="#fff" stroke-width="1"/></svg>
        </li>
        <li>www.terrawise.co
          <svg viewBox="0 0 18 18" aria-hidden="true"><rect width="18" height="18" rx="3" fill="#fff"/><circle cx="9" cy="9" r="5" fill="none" stroke="#14c22c" stroke-width="1.3"/><path d="M4 9h10M9 4c-2.5 3-2.5 7 0 10M9 4c2.5 3 2.5 7 0 10" fill="none" stroke="#14c22c" stroke-width="1"/></svg>
        </li>
      </ul>
    </div>
  </div>

  <div class="band back__bottom"></div>
</section>

</body>
</html>
```